Infographic for Anesthesia Management Company

I would like my Anesthesia Management company, Veltrin Anesthesia, service information placed into a infographic for use on a brochure and webpage. Please focus on just the infographic.
-Veltrin Services text to be placed into infographic attached in word file.
-Two Vector infographic templates attached as well. I am open to either option, or alternative layout suggestion.
-Please match color scheme to veltrinanesthesia-example.com
-Veltrin logo attached.
Thank you for your help!
Marvin
Target Market(s)
Surgery Centers
Industry/Entity Type
It Company
Font styles to use
Requirements
Must have
- Professional Look.
- Easy to read text.
- Cohesive branding
Nice to have
- Please see attached Vector examples.

```html
<!DOCTYPE html>
<html lang="en">
<head>
<meta charset="utf-8">
<title>Veltrin Anesthesia – Provider Recruitment, Credentialing, and Staffing</title>
<link href="https://fonts.googleapis.com/css2?family=Roboto:wght@700&family=Roboto+Condensed:wght@400;700&display=swap" rel="stylesheet">
<style>
  :root {
    --bg: #ffffff;
    --title: #414042;
    --purple: #837093;
    --purple-fold: #5a4a66;
    --purple-box: #433848;
    --purple-head: #b7a6c6;
    --teal: #1dbba0;
    --teal-fold: #117a68;
    --teal-box: #0a2e28;
    --teal-head: #8ee6d4;
    --ink-light: #ffffff;
  }
  html, body { margin: 0; padding: 0; overflow: hidden; background: var(--bg); }
  .canvas { position: relative; width: 1200px; height: 814px; overflow: hidden; background: var(--bg); }
  .stage {
    position: absolute; left: 0; top: 0; width: 1050px; height: 712px;
    transform: scale(1.142857); transform-origin: 0 0;
  }
  .shapes { position: absolute; inset: 0; }
  .title {
    position: absolute; left: 0; right: 0; top: 70px; margin: 0;
    text-align: center; font: 700 28px/1.2 "Roboto", sans-serif; color: var(--title);
    letter-spacing: -0.2px;
  }
  .pillar-label { position: absolute; left: 251px; width: 210px; font-family: "Roboto Condensed", sans-serif; }
  .pillar-name { margin: 0 0 4px; font-weight: 700; font-size: 16px; text-transform: uppercase; }
  .pillar-theme { margin: 0; font-size: 17px; line-height: 1.25; color: var(--ink-light); }
  .pillar-purple .pillar-name { color: var(--purple-head); }
  .pillar-teal .pillar-name { color: var(--teal-head); }
  .detail {
    position: absolute; left: 514px; width: 420px;
    font: 400 13.3px/1.3 "Roboto Condensed", sans-serif; color: var(--ink-light);
  }
  .detail ul { margin: 0; padding: 0; list-style: none; }
  .detail li { position: relative; padding-left: 16px; }
  .detail li::before { content: "•"; position: absolute; left: 2px; font-size: 10px; top: 1px; }
  .detail-sub { margin: 3px 0 4px 14px; font-weight: 700; }
</style>
</head>
<body>
<div class="canvas">
  <div class="stage">
    <svg class="shapes" viewBox="0 0 1050 712" width="1050" height="712" aria-hidden="true">
      <!-- row 1 -->
      <polygon points="52,137 215,137 215,265 52,265 110,201" fill="var(--purple)"/>
      <polygon points="215,137 232,162 232,276 215,265" fill="var(--purple-fold)"/>
      <rect x="232" y="162" width="236" height="114" fill="var(--purple-box)"/>
      <polygon points="468,162 485,137 485,265 468,276" fill="var(--purple-fold)"/>
      <polygon points="485,137 960,137 1000,201 960,265 485,265" fill="var(--purple)"/>
      <!-- row 2 -->
      <polygon points="52,265 215,265 215,393 52,393 110,329" fill="var(--teal)"/>
      <polygon points="215,265 232,276 232,393 215,393" fill="var(--teal-fold)"/>
      <rect x="232" y="276" width="236" height="117" fill="var(--teal-box)"/>
      <polygon points="468,276 485,265 485,393 468,393" fill="var(--teal-fold)"/>
      <polygon points="485,265 960,265 1000,329 960,393 485,393" fill="var(--teal)"/>
      <!-- row 3 -->
      <polygon points="52,393 215,393 215,521 52,521 110,457" fill="var(--purple)"/>
      <polygon points="215,393 232,393 232,508 215,521" fill="var(--purple-fold)"/>
      <rect x="232" y="393" width="236" height="115" fill="var(--purple-box)"/>
      <polygon points="468,393 485,393 485,521 468,508" fill="var(--purple-fold)"/>
      <polygon points="485,393 960,393 1000,457 960,521 485,521" fill="var(--purple)"/>
      <!-- row 4 -->
      <polygon points="52,521 215,521 215,649 52,649 110,585" fill="var(--teal)"/>
      <polygon points="215,521 232,508 232,622 215,649" fill="var(--teal-fold)"/>
      <rect x="232" y="508" width="236" height="114" fill="var(--teal-box)"/>
      <polygon points="468,508 485,521 485,649 468,622" fill="var(--teal-fold)"/>
      <polygon points="485,521 960,521 1000,585 960,649 485,649" fill="var(--teal)"/>

      <!-- icons -->
      <g fill="none" stroke="#fff" stroke-width="1.6" stroke-linecap="round" stroke-linejoin="round">
        <!-- clinician -->
        <path d="M141,180 q14,-10 28,0 v10 h-28 z"/>
        <path d="M155,181 v6 M152,184 h6"/>
        <path d="M141,192 q0,20 14,22 q14,-2 14,-22"/>
        <path d="M122,242 v-10 q0,-12 18,-16 l15,10 l15,-10 q18,4 18,16 v10"/>
        <path d="M166,236 h8"/>
        <!-- medical kit -->
        <rect x="124" y="308" width="62" height="48" rx="3"/>
        <path d="M144,308 v-7 h22 v7"/>
        <path d="M150,322 h10 v8 h8 v10 h-8 v8 h-10 v-8 h-8 v-10 h8 z"/>
        <!-- heart pulse -->
        <path d="M155,484 l-26,-26 a15,15 0 0 1 26,-22 a15,15 0 0 1 26,22 z"/>
        <path d="M122,460 h20 l5,-10 l6,22 l6,-26 l5,14 h28"/>
        <!-- hands holding person -->
        <circle cx="155" cy="552" r="8"/>
        <path d="M141,582 v-8 q0,-10 14,-12 q14,2 14,12 v8"/>
        <path d="M124,576 v-14 q4,-4 6,0 v14 l10,10 v14"/>
        <path d="M186,576 v-14 q-4,-4 -6,0 v14 l-10,10 v14"/>
      </g>
    </svg>

    <h1 class="title">Anesthesia Provider Recruitment, Credentialing, And Staffing</h1>

    <div class="pillar-label pillar-purple" style="top:200px">
      <p class="pillar-name">Professionalism</p>
      <p class="pillar-theme">ASC Stakeholder Satisfaction</p>
    </div>
    <div class="detail" style="top:170px">
      <ul>
        <li>Share our personal network of highly qualified anesthesia providers</li>
        <li>Create continuity between anesthesia, surgeon, and ASC staff</li>
        <li>Guarantee every anesthesia provider upholds clinical excellence</li>
        <li>Coordinate staffing to meet your scheduled case volume</li>
      </ul>
    </div>

    <div class="pillar-label pillar-teal" style="top:300px">
      <p class="pillar-name">Accountability</p>
      <p class="pillar-theme">Meeting Accreditation Requirements</p>
    </div>
    <div class="detail" style="top:280px">
      <ul>
        <li>Partner with your surgery center to ensure anesthesia policies and procedures are up to current ASC credentialing standards</li>
      </ul>
      <p class="detail-sub">In-House Billing</p>
      <ul>
        <li>Dedicated in-house billers ensure anesthesia billing is processed correctly the first time</li>
      </ul>
    </div>

    <div class="pillar-label pillar-purple" style="top:428px">
      <p class="pillar-name">Efficiency</p>
      <p class="pillar-theme">Thought Leadership</p>
    </div>
    <div class="detail" style="top:419px">
      <ul>
        <li>Stipend free anesthesia services</li>
        <li>Proprietary and data-driven process to maintain on-time surgery flow</li>
      </ul>
    </div>

    <div class="pillar-label pillar-teal" style="top:533px">
      <p class="pillar-name">Patient Safety</p>
      <p class="pillar-theme">Clinical Guidance and Quality Improvement</p>
    </div>
    <div class="detail" style="top:537px">
      <ul>
        <li>Pre-operative protocols to minimize cancellations and optimize patient outcomes</li>
        <li>Patient selection criteria to ensure suitable surgical candidates</li>
        <li>Education programs to engage the clinical staff</li>
        <li>Evidence based multimodal pain management protocol to facilitate a timely discharge and reduce patient side effects</li>
      </ul>
    </div>
  </div>
</div>
</body>
</html>
```